Biz Card for Harrowfield Property Partners - HWPP

Harrowfield Property Partners is a commercial real estate acquisitions firm. We buy commercial property and need to raise capital from investors for each deal we buy. The vibe needs to be: give us your money, we will multiply it.
Our website: www.hrwpp-example.com
Competitors are: https://velmarholdings-example.com/, https://tribanquepartners-example.com/, http://www.ostrellecapital-example.com/
Target Market(s)
High Net Worth Individuals, Bankers, Insurance Companies, Commercial Real Estate Brokers.
Industry/Entity Type
Investment Banking
Contact Information for Business Card
Name, Title, Addess, Cell#, Office#, email, website
Requirements
Must have
- use one of our logos. See website for look and feel: www.hrwpp-example.com
Nice to have
- see website: www.hrwpp-example.com

```html
<!DOCTYPE html>
<html lang="en">
<head>
<meta charset="utf-8">
<title>Harrowfield Property Partners – Business Card</title>
<link rel="stylesheet" href="https://fonts.googleapis.com/css2?family=Poppins:wght@400;500&family=Lato:wght@300;400&display=swap">
<style>
  :root {
    --navy: #01243f;
    --ink: #0d2237;
    --paper: #ffffff;
    --stage: #b3b3b3;
    --rule-light: #e9eef3;
    --muted: #9fb0c0;
  }
  html, body {
    margin: 0;
    width: 1200px;
    height: 900px;
    overflow: hidden;
    background: var(--stage);
  }
  .stage { position: relative; width: 1200px; height: 900px; }

  .card {
    position: absolute;
    top: 294px;
    width: 513px;
    height: 300px;
    box-sizing: border-box;
    overflow: hidden;
  }

  /* Front */
  .card-front {
    left: 66px;
    background: var(--paper);
    color: var(--ink);
    font-family: "Poppins", sans-serif;
  }
  .front-rule {
    position: absolute; left: 0; right: 0; top: 30px;
    height: 2px; background: var(--navy);
  }
  .holder { position: absolute; left: 37px; top: 42px; }
  .holder-name { margin: 0; font-size: 13.5px; font-weight: 500; line-height: 18px; }
  .holder-title { margin: 1px 0 0; font-size: 10.5px; font-weight: 400; line-height: 14px; }

  .contacts {
    position: absolute; left: 37px; top: 158px;
    margin: 0; padding: 0; list-style: none;
    font-size: 10.2px; line-height: 16px;
  }
  .contacts li { display: flex; align-items: center; }
  .contacts svg { width: 9px; height: 9px; margin-right: 7px; flex: none; fill: var(--ink); }
  .contacts .address { align-items: flex-start; margin-top: 9px; }
  .contacts .address svg { margin-top: 3px; }

  .front-mark {
    position: absolute; left: 307px; top: 161px; width: 200px;
    text-align: center;
  }
  .mark-dot {
    display: block; margin: 0 auto 8px;
    width: 60px; height: 60px; border-radius: 50%;
    background: var(--navy);
  }
  .mark-name {
    margin: 0; font-size: 12px; font-weight: 400;
    letter-spacing: 2.4px; line-height: 17px; color: var(--navy);
    text-transform: uppercase;
  }

  /* Back */
  .card-back {
    left: 618px; width: 511px;
    background: var(--navy);
    color: var(--paper);
    font-family: "Lato", sans-serif;
  }
  .back-name {
    position: absolute; left: 33px; top: 180px;
    margin: 0; font-size: 17px; font-weight: 300;
    letter-spacing: 4px; line-height: 22px;
    text-transform: uppercase;
  }
  .back-rule {
    position: absolute; left: 0; right: 0; top: 246px;
    height: 1.5px; background: var(--rule-light);
  }
  .back-url {
    position: absolute; right: 34px; top: 254px;
    margin: 0; font-size: 10.5px; font-weight: 400;
    letter-spacing: 0.8px; text-transform: uppercase;
  }
</style>
</head>
<body>
<main class="stage">

  <section class="card card-front" aria-label="Business card front">
    <div class="front-rule"></div>

    <div class="holder">
      <p class="holder-name">Dorian Whitcombe</p>
      <p class="holder-title">CEO/Founder</p>
    </div>

    <ul class="contacts">
      <li>
        <svg viewBox="0 0 10 10" aria-hidden="true"><path d="M2.5 0h5a1 1 0 0 1 1 1v8a1 1 0 0 1-1 1h-5a1 1 0 0 1-1-1V1a1 1 0 0 1 1-1zm.4 1.2v6.4h4.2V1.2zM5 8.2a.55.55 0 1 0 0 1.1.55.55 0 0 0 0-1.1z"/></svg>
        800-555-0142
      </li>
      <li>
        <svg viewBox="0 0 10 10" aria-hidden="true"><path d="M2 .3l1.6 2.2-.9 1.2c.6 1.2 1.5 2.1 2.7 2.7l1.2-.9L8.8 7l-.6 1.9C4.4 9 .9 5.6 1 1.8z"/></svg>
        (786) 555-0193
      </li>
      <li>
        <svg viewBox="0 0 10 10" aria-hidden="true"><path d="M.5 2h9v6h-9zM1.3 2.6L5 5.4l3.7-2.8z" fill-rule="evenodd"/></svg>
        info@hrwpp-example.com
      </li>
      <li>
        <svg viewBox="0 0 10 10" aria-hidden="true"><path d="M5 .5a4.5 4.5 0 1 0 0 9 4.5 4.5 0 0 0 0-9zm0 1c.5.5.9 1.5 1 2.8H4c.1-1.3.5-2.3 1-2.8zM3.2 4.3H1.6A3.5 3.5 0 0 1 3.6 1.8c-.3.7-.4 1.6-.4 2.5zm0 1.4c0 .9.1 1.8.4 2.5a3.5 3.5 0 0 1-2-2.5zm.8 0h2c-.1 1.3-.5 2.3-1 2.8-.5-.5-.9-1.5-1-2.8zm2.8 0h1.6a3.5 3.5 0 0 1-2 2.5c.3-.7.4-1.6.4-2.5zm0-1.4c0-.9-.1-1.8-.4-2.5a3.5 3.5 0 0 1 2 2.5z"/></svg>
        www.hrwpp-example.com
      </li>
      <li class="address">
        <svg viewBox="0 0 10 10" aria-hidden="true"><path d="M5 0a3.5 3.5 0 0 0-3.5 3.5C1.5 6 5 10 5 10s3.5-4 3.5-6.5A3.5 3.5 0 0 0 5 0zm0 2.2a1.3 1.3 0 1 1 0 2.6 1.3 1.3 0 0 1 0-2.6z"/></svg>
        <span>418 Meridian Ave, Suite 902<br>Coral Gables, FL 33146</span>
      </li>
    </ul>

    <div class="front-mark">
      <span class="mark-dot" aria-hidden="true"></span>
      <p class="mark-name">Harrowfield<br>Property Partners</p>
    </div>
  </section>

  <section class="card card-back" aria-label="Business card back">
    <p class="back-name">Harrowfield<br>Property Partners</p>
    <div class="back-rule"></div>
    <p class="back-url">www.hrwpp-example.com</p>
  </section>

</main>
</body>
</html>
```